The Wellness Barn Business Card

Info for the front..... (in whichever order and layout looks best)
Carla Penhallow
Physiotherapist
4/37 Upper Creekbank Rd
Tallowbrook
QLD 4712
0462305178
carlapenhallow57@mailbox.example
www.thewellnessbarn.example.au
on the back I would like to be able to write appointments so probably just that heading with lines.
I like a sort of rustic style but mostly professional, colours in naturals, beige, brown, green etc. I dont mind if the logo colour is changed slightly to suit.

```html
<!DOCTYPE html>
<html lang="en">
<head>
<meta charset="utf-8">
<title>The Wellness Barn – Business Card</title>
<link href="https://fonts.googleapis.com/css2?family=Poppins:wght@400;500;600;700;800&display=swap" rel="stylesheet">
<style>
  :root {
    --forest: #2d4323;
    --bark: #8b5229;
    --paper: #ffffff;
    --backdrop: #f3f3f4;
    --rule: #dcdcdc;
    --ink-soft: #555555;
  }
  * { margin: 0; padding: 0; box-sizing: border-box; }
  html, body { width: 1200px; height: 3090px; overflow: hidden; }
  body {
    background: var(--backdrop);
    font-family: "Poppins", Arial, sans-serif;
    position: relative;
  }
  .card {
    position: absolute;
    left: 192px;
    width: 816px;
    background: var(--paper);
    box-shadow: 0 30px 50px rgba(0,0,0,0.10);
  }

  /* Front */
  .card-front { top: 182px; height: 467px; }
  .brand-name {
    position: absolute;
    left: 0; right: 0; top: 170px;
    text-align: center;
    color: var(--forest);
    font-weight: 800;
    font-size: 56px;
    line-height: 1.1;
    letter-spacing: -0.5px;
  }
  .website {
    position: absolute;
    left: 0; right: 0; top: 398px;
    text-align: center;
    color: var(--bark);
    font-size: 22px;
    white-space: nowrap;
  }
  .website strong { font-weight: 700; }
  .front-band {
    position: absolute;
    left: 0; right: 0; bottom: 0;
    height: 13px;
    display: flex;
  }
  .front-band .band-green { width: 403px; background: var(--forest); }
  .front-band .band-brown { flex: 1; background: var(--bark); }

  /* Back */
  .card-back { top: 716px; height: 466px; }
  .profile-panel {
    position: absolute;
    left: 0; top: 0; bottom: 0;
    width: 357px;
    background: var(--forest);
    color: var(--paper);
  }
  .person-name {
    position: absolute;
    left: 59px; top: 74px;
    font-size: 33px;
    font-weight: 500;
    white-space: nowrap;
  }
  .person-name b { font-weight: 700; }
  .person-role {
    position: absolute;
    left: 59px; top: 114px;
    font-size: 22px;
  }
  .name-rule {
    position: absolute;
    left: 59px; top: 158px;
    width: 264px; height: 3px;
    background: var(--paper);
  }
  .contact-box {
    position: absolute;
    left: 26px; top: 244px;
    width: 365px; height: 152px;
    background: var(--bark);
    color: var(--paper);
    padding: 30px 0 0 0;
  }
  .contact-row {
    display: flex;
    align-items: flex-start;
    font-size: 16.5px;
    line-height: 20px;
    margin-bottom: 7px;
    white-space: nowrap;
  }
  .contact-row svg { margin: 2px 0 0 30px; width: 15px; height: 15px; flex: none; }
  .contact-row span { margin-left: 19px; }
  .contact-row.email { font-size: 15px; }

  .appointment {
    position: absolute;
    left: 413px; top: 0; width: 403px; bottom: 0;
    color: var(--bark);
  }
  .appointment h2 {
    position: absolute;
    left: 0; top: 56px;
    font-size: 31px;
    font-weight: 700;
    letter-spacing: -0.3px;
    white-space: nowrap;
  }
  .field-label {
    position: absolute;
    left: 0;
    font-size: 18px;
    white-space: nowrap;
  }
  .field-line {
    position: absolute;
    height: 1px;
    background: var(--rule);
    right: 50px;
  }
  .weekdays {
    position: absolute;
    top: 418px;
    left: 0;
    width: 403px;
    height: 20px;
    font-size: 13px;
    line-height: 20px;
    color: var(--ink-soft);
  }
  .weekday {
    position: absolute;
    top: 0;
    white-space: nowrap;
  }
  .weekday::before {
    content: "";
    display: inline-block;
    width: 4px; height: 4px;
    border-radius: 50%;
    background: var(--bark);
    margin-right: 7px;
    vertical-align: middle;
  }
</style>
</head>
<body>

  <section class="card card-front">
    <div class="brand-name">The Wellness<br>Barn</div>
    <div class="website">www.<strong>thewellnessbarn.example</strong>.au</div>
    <div class="front-band"><div class="band-green"></div><div class="band-brown"></div></div>
  </section>

  <section class="card card-back">
    <div class="profile-panel">
      <div class="person-name"><b>Carla</b> Penhallow</div>
      <div class="person-role">Physiotherapist</div>
      <div class="name-rule"></div>
    </div>

    <div class="contact-box">
      <div class="contact-row">
        <svg viewBox="0 0 16 16" fill="none" stroke="#fff" stroke-width="1.2"><path d="M8 15s5-5 5-9a5 5 0 0 0-10 0c0 4 5 9 5 9z"/><circle cx="8" cy="6" r="1.8"/></svg>
        <span>4/37 Upper Creekbank Rd,<br>Tallowbrook, QLD 4712</span>
      </div>
      <div class="contact-row">
        <svg viewBox="0 0 16 16" fill="none" stroke="#fff" stroke-width="1.2"><path d="M3 1.5l2.5 0 1.2 3-1.6 1.3a8 8 0 0 0 4.8 4.8l1.3-1.6 3 1.2v2.5a1.5 1.5 0 0 1-1.6 1.5A12.5 12.5 0 0 1 1.5 3.1 1.5 1.5 0 0 1 3 1.5z"/></svg>
        <span>0462305178</span>
      </div>
      <div class="contact-row email">
        <svg viewBox="0 0 16 16" fill="none" stroke="#fff" stroke-width="1.2"><rect x="1.5" y="3.5" width="13" height="9"/><path d="M1.5 3.5l6.5 5 6.5-5M1.5 12.5l4.5-4M14.5 12.5l-4.5-4"/></svg>
        <span>carlapenhallow57@mailbox.example</span>
      </div>
    </div>

    <div class="appointment">
      <h2>APPOINTMENT</h2>
      <div class="field-label" style="top:136px">NAME :</div>
      <div class="field-line" style="left:79px; top:154px"></div>
      <div class="field-line" style="left:1px; top:195px"></div>
      <div class="field-line" style="left:1px; top:239px"></div>
      <div class="field-label" style="top:273px">DATE :</div>
      <div class="field-line" style="left:80px; top:293px"></div>
      <div class="field-label" style="top:320px">TIME :</div>
      <div class="field-line" style="left:80px; top:340px"></div>
      <div class="weekdays">
        <span class="weekday" style="left:11px">MON</span>
        <span class="weekday" style="left:93px">TUE</span>
        <span class="weekday" style="left:174px">WED</span>
        <span class="weekday" style="left:254px">THU</span>
        <span class="weekday" style="left:330px">FRI</span>
      </div>
    </div>
  </section>

</body>
</html>
```